Business Card

I would like a business card with a picture of my husband and I that is unique and professional.

Industry/Entity Type

Business

Font styles to use
Serif

```html
<!DOCTYPE html>
<html lang="en">
<head>
<meta charset="utf-8">
<title>Harlow Leadership Group — Business Card</title>
<link href="https://fonts.googleapis.com/css2?family=Open+Sans:wght@400;600;700&display=swap" rel="stylesheet">
<style>
  :root {
    --backdrop: #ecebe8;
    --card: #ffffff;
    --gold: #f6be62;
    --ink: #222222;
    --muted: #7a7a7a;
    --shadow: rgba(0, 0, 0, 0.28);
  }
  * { margin: 0; padding: 0; box-sizing: border-box; }
  html, body {
    width: 1200px; height: 900px; overflow: hidden;
    background: var(--backdrop);
    font-family: "Open Sans", Arial, sans-serif;
    color: var(--ink);
  }
  .canvas { position: relative; width: 1200px; height: 900px; }
  .card {
    position: absolute; width: 620px; height: 364px;
    background: var(--card); overflow: hidden;
    box-shadow: 6px 8px 14px var(--shadow);
  }
  .card svg.shapes { position: absolute; inset: 0; }

  /* front */
  .card-front { left: 44px; top: 44px; border-top-right-radius: 60px; }
  .brand {
    position: absolute; left: 40px; top: 130px; width: 230px;
    display: flex; flex-direction: column; align-items: center; gap: 12px;
  }
  .brand-row { display: flex; align-items: center; gap: 10px; }
  .brand-dot { width: 18px; height: 18px; border-radius: 50%; background: var(--gold); }
  .brand-initials { font-size: 46px; font-weight: 700; color: var(--ink); letter-spacing: 4px; line-height: 1; }
  .brand-name {
    font-size: 11px; font-weight: 700; color: var(--ink);
    letter-spacing: 1px; text-transform: uppercase;
    border-top: 1px solid var(--ink); border-bottom: 1px solid var(--ink);
    padding: 3px 0; white-space: nowrap;
  }

  /* back */
  .card-back { left: 520px; top: 480px; border-top-left-radius: 70px; }
  .web {
    position: absolute; left: 30px; top: 182px;
    transform: translate(-50%, -50%) rotate(90deg);
    font-size: 15px; color: var(--ink); white-space: nowrap;
  }
  .brand-small {
    position: absolute; right: 30px; top: 40px; width: 170px;
    display: flex; flex-direction: column; align-items: center; gap: 8px;
  }
  .brand-small .brand-initials { font-size: 32px; letter-spacing: 3px; }
  .brand-small .brand-dot { width: 12px; height: 12px; }
  .brand-small .brand-name { font-size: 8px; letter-spacing: 0.6px; }
  .person { position: absolute; left: 190px; top: 180px; }
  .person-name { font-size: 28px; font-weight: 700; line-height: 1.1; white-space: nowrap; }
  .person-role { font-size: 13px; margin-top: 6px; }
  .person-email { font-size: 13px; color: var(--muted); }
  .contacts {
    position: absolute; left: 200px; top: 284px;
    display: flex; gap: 22px; font-size: 14px; line-height: 24px; white-space: nowrap;
  }
  .phones .label { color: var(--gold); font-weight: 700; margin-right: 4px; }
  .address { border-left: 1px solid var(--ink); padding-left: 22px; }
</style>
</head>
<body>
<main class="canvas">

  <section class="card card-front">
    <svg class="shapes" width="620" height="364" viewBox="0 0 620 364">
      <polygon points="326,0 346,0 306,364 286,364" fill="var(--gold)"/>
      <defs>
        <linearGradient id="photoTone" x1="0" y1="0" x2="1" y2="1">
          <stop offset="0" stop-color="#ece9e6"/>
          <stop offset="0.55" stop-color="#8d7a6c"/>
          <stop offset="1" stop-color="#5d5f66"/>
        </linearGradient>
      </defs>
      <polygon role="img" aria-label="Portrait photograph of the couple, smiling, in business attire"
               points="346,0 620,0 620,364 306,364" fill="url(#photoTone)"/>
    </svg>
    <div class="brand">
      <div class="brand-row">
        <span class="brand-dot"></span>
        <span class="brand-initials">HLG</span>
      </div>
      <div class="brand-name">Harlow Leadership Group</div>
    </div>
  </section>

  <section class="card card-back">
    <svg class="shapes" width="620" height="364" viewBox="0 0 620 364">
      <polygon points="0,0 78,0 150,364 0,364" fill="var(--gold)"/>
      <polygon points="78,0 92,0 164,364 150,364" fill="var(--ink)"/>
    </svg>
    <div class="web">www.hlgroup.com</div>
    <div class="brand-small">
      <div class="brand-row">
        <span class="brand-dot"></span>
        <span class="brand-initials">HLG</span>
      </div>
      <div class="brand-name">Harlow Leadership Group</div>
    </div>
    <div class="person">
      <div class="person-name">Marcus Hale</div>
      <div class="person-role">Director</div>
      <div class="person-email">marcus@hlgroup.com</div>
    </div>
    <div class="contacts">
      <div class="phones">
        <div><span class="label">m.</span>0700-48261</div>
        <div><span class="label">t.</span>0700-48262</div>
      </div>
      <div class="address">
        <div>14 Linden Road</div>
        <div>Brookfield 55210</div>
      </div>
    </div>
  </section>

</main>
</body>
</html>
```